metal roofing website

I have several domain names and a website that has been built. I need someone to recreate essentially the same website and change some photos and basic design to create the new sites. I have all of the files and c panel access to the lucky winner. If you can do a good job at a fair price I will have 100's of sites to send to you very soon. I have the site built and have all files just need it recreated on my server. the current site is www.brantlepanelinc.com I am looking to get this done ASAP!!!

```html
<!DOCTYPE html>
<html lang="en">
<head>
<meta charset="utf-8">
<title>Brantle Panel – Metal Roofing & Post Frame Buildings</title>
<link rel="stylesheet" href="https://fonts.googleapis.com/css2?family=Raleway:wght@500;600;700;800&family=Open+Sans:wght@400;600;700&display=swap">
<style>
:root{
  --red:#b82a24;
  --red-dark:#9e221d;
  --sand:#e0d4c2;
  --taupe:#a89c8c;
  --yellow:#f5c400;
  --ink:#222;
  --charcoal:#2a2a2a;
  --coal:#1f1f1f;
  --white:#fff;
  --muted:#6d665d;
}
*{box-sizing:border-box;margin:0;padding:0}
html,body{width:1200px;height:2590px;overflow:hidden}
body{position:relative;font-family:"Open Sans",sans-serif;color:var(--ink);background:var(--sand)}
.abs{position:absolute}
.center{text-align:center}
.btn{position:absolute;display:flex;align-items:center;justify-content:center;border-radius:20px;font-family:"Raleway",sans-serif;font-weight:700;font-size:10px;letter-spacing:.5px;color:var(--white);text-transform:uppercase}
.btn-red{background:var(--red)}
.btn-ghost{border:2px solid var(--white)}
.btn-yellow{background:var(--yellow);color:var(--ink)}
.heading{font-family:"Raleway",sans-serif;font-weight:700;text-transform:uppercase;width:100%;text-align:center;position:absolute}
.heading-rule{position:absolute;left:582px;width:36px;height:2px;background:var(--red)}

/* top bar */
.topbar{top:0;left:0;width:1200px;height:31px;background:var(--red);color:var(--white);font-size:10px;display:flex;align-items:center;justify-content:flex-end;gap:22px;padding-right:234px}
.topbar span{display:flex;align-items:center;gap:6px}

/* hero */
.hero{top:31px;left:0;width:1200px;height:465px;background:linear-gradient(180deg,#8f9aa0 0%,#b6b1a6 38%,#8b8170 62%,#4f6b34 82%,#3e5a28 100%)}
.hero-shade{top:31px;left:0;width:1200px;height:465px;background:rgba(0,0,0,.18)}
.logo-box{top:0;left:235px;width:105px;height:100px;background:var(--sand);display:flex;flex-direction:column;align-items:center;justify-content:center;gap:4px}
.logo-name{font-family:"Raleway",sans-serif;font-weight:800;font-size:14px;color:var(--red);text-align:center;line-height:1.05;text-transform:uppercase}
.logo-mark{width:10px;height:10px;background:var(--red)}
.nav{top:52px;left:490px;display:flex;gap:24px;font-family:"Raleway",sans-serif;font-weight:600;font-size:10px;color:var(--white);text-transform:uppercase}
.hero-title{top:262px;width:1200px;text-align:center;font-family:"Raleway",sans-serif;font-weight:800;font-size:29px;color:var(--white);text-transform:uppercase}
.hero-rule{top:284px;height:2px;width:58px;background:var(--red)}

.tabs{top:432px;left:235px;display:flex;gap:19px}
.tab{width:169px;height:78px;background:var(--taupe);padding:16px 16px 0;color:var(--white);position:relative}
.tab.is-active{background:var(--red)}
.tab h3{font-family:"Raleway",sans-serif;font-weight:700;font-size:15px;line-height:1.2;text-transform:uppercase}
.tab .more{position:absolute;bottom:10px;left:16px;font-size:9px;font-weight:700}
.tab.is-active::before{content:"";position:absolute;top:-8px;left:74px;border:8px solid transparent;border-top:0;border-bottom-color:var(--red)}

/* services */
.card{top:646px;width:232px;height:268px;background:var(--white);box-shadow:0 2px 8px rgba(0,0,0,.08)}
.card-photo{height:159px}
.card h4{font-family:"Raleway",sans-serif;font-weight:700;font-size:11px;text-transform:uppercase;text-align:center;margin-top:22px;line-height:1.3}
.card p{font-size:10px;color:var(--muted);text-align:center;line-height:1.45;margin:4px 30px 0}

/* stats */
.stats{top:1031px;left:0;width:1200px;height:187px;background:var(--red)}
.stat{position:absolute;top:65px;width:180px;margin-left:-90px;text-align:center;color:var(--white)}
.stat b{display:block;font-family:"Open Sans",sans-serif;font-weight:700;font-size:28px;line-height:1}
.stat span{display:block;font-size:10px;font-weight:600;margin-top:14px}

/* projects */
.projects-head{top:1218px;left:0;width:1200px;height:127px;background:linear-gradient(90deg,#1c1c1c,#2c2e2c 60%,#3a3a36)}
.grid{top:1345px;left:0;width:1200px;display:grid;grid-template-columns:repeat(4,300px);grid-auto-rows:199px}
.projects-foot{top:1743px;left:0;width:1200px;height:126px;background:linear-gradient(180deg,#2a2a28,#3b3b38)}

/* clients */
.clients{top:1869px;left:0;width:1200px;height:376px;background:var(--charcoal);color:var(--white)}
.avatar{position:absolute;border-radius:50%;background:radial-gradient(circle at 50% 40%,#c9b3a2,#6d5a4e)}
.dot{position:absolute;top:310px;width:6px;height:6px;border-radius:50%;background:#999}

/* contact band */
.contact-band{top:2245px;left:0;width:1200px;height:95px;background:var(--red);color:var(--white)}
.contact-item{position:absolute;top:26px;display:flex;gap:14px;align-items:center}
.contact-item small{display:block;font-family:"Raleway",sans-serif;font-weight:700;font-size:11px;text-transform:uppercase}
.contact-item strong{display:block;font-family:"Raleway",sans-serif;font-weight:700;font-size:21px}
.follow{top:38px;left:853px;display:flex;align-items:center;gap:9px;font-family:"Raleway",sans-serif;font-weight:700;font-size:11px}
.follow i{display:block;width:12px;height:12px;border-radius:50%;background:var(--white)}

/* footer */
.footer{top:2340px;left:0;width:1200px;height:221px;background:var(--sand)}
.footer h5{position:absolute;top:56px;font-family:"Raleway",sans-serif;font-weight:700;font-size:13px;text-transform:uppercase}
.footer ul{position:absolute;top:85px;list-style:none;font-size:10px;color:var(--muted)}
.footer ul li{margin-bottom:11px;white-space:nowrap}
.hours{position:absolute;left:807px;top:85px;width:158px;font-size:9px;color:var(--muted)}
.hours p{line-height:1.5;margin-bottom:8px}
.hours div{display:flex;justify-content:space-between;margin-bottom:6px}
.hours div b{color:var(--ink);font-weight:400}
.bottombar{top:2561px;left:0;width:1200px;height:29px;background:var(--coal);color:#aaa;font-size:9px;display:flex;align-items:center;justify-content:space-between;padding:0 234px}
.bottombar nav{display:flex;gap:14px}
</style>
</head>
<body>

<div class="abs topbar">
  <span><svg width="10" height="10" viewBox="0 0 24 24"><path fill="#fff" d="M6.6 10.8a15 15 0 0 0 6.6 6.6l2.2-2.2c.3-.3.7-.4 1-.2 1.1.4 2.3.6 3.6.6.6 0 1 .4 1 1V20c0 .6-.4 1-1 1A17 17 0 0 1 3 4c0-.6.4-1 1-1h3.5c.6 0 1 .4 1 1 0 1.3.2 2.5.6 3.6.1.3 0 .7-.2 1z"/></svg>715-555-0142</span>
  <span><svg width="11" height="9" viewBox="0 0 24 18"><path fill="#fff" d="M0 0h24v18H0zM2 2l10 7 10-7z" fill-rule="evenodd"/></svg>info@example.com</span>
  <span><svg width="8" height="11" viewBox="0 0 16 22"><path fill="#fff" d="M8 0a8 8 0 0 0-8 8c0 6 8 14 8 14s8-8 8-14a8 8 0 0 0-8-8zm0 11a3 3 0 1 1 0-6 3 3 0 0 1 0 6z"/></svg>Building Park, New York, NY 10001</span>
</div>

<header>
  <div class="abs hero" role="img" aria-label="Photo of a large tan post frame house with wraparound porch on a green lawn"></div>
  <div class="abs hero-shade"></div>
  <div class="abs logo-box">
    <div class="logo-mark"></div>
    <div class="logo-name">Brantle<br>Panel</div>
  </div>
  <nav class="abs nav"><span>Home</span><span>About Us</span><span>Services</span><span>Gallery</span><span>Contact Us</span></nav>
  <div class="btn btn-yellow" style="top:46px;left:868px;width:105px;height:30px">Get a Quote</div>
  <div class="abs hero-rule" style="left:350px"></div>
  <div class="abs hero-rule" style="left:792px"></div>
  <h1 class="abs hero-title">Complete Post Frame</h1>
  <div class="btn btn-red" style="top:328px;left:500px;width:106px;height:30px">Get a Quote</div>
  <div class="btn btn-ghost" style="top:328px;left:635px;width:106px;height:30px">Visualizer</div>
  <div class="abs tabs">
    <div class="tab is-active"><h3>Complete Post<br>Frame</h3><span class="more">Read More ➞</span></div>
    <div class="tab"><h3>Residential</h3><span class="more">Read More ➞</span></div>
    <div class="tab"><h3>Prefab Sheets</h3><span class="more">Read More ➞</span></div>
    <div class="tab"><h3>Agricultural &amp;<br>Commercial</h3><span class="more">Read More ➞</span></div>
  </div>
</header>

<section>
  <h2 class="heading" style="top:588px;font-size:16px">Our Services</h2>
  <div class="heading-rule" style="top:613px"></div>
  <article class="abs card" style="left:235px">
    <div class="card-photo" role="img" aria-label="Photo of a grey steel post frame building under blue sky" style="background:linear-gradient(180deg,#4d86c9,#8fb3da 55%,#7b7b76 70%,#8c7a5f)"></div>
    <h4>Complete Post<br>Frame Building Packages</h4>
    <p>Call us for a quote, or stop in and we can help you design</p>
  </article>
  <article class="abs card" style="left:485px">
    <div class="card-photo" role="img" aria-label="Photo of a red garage with metal roof among trees" style="background:linear-gradient(180deg,#c9d3c6,#7a2a22 55%,#8a3028 75%,#6d7a4e)"></div>
    <h4>Residential<br>Metal Roofing</h4>
    <p>Super rib, snap-loc and a variety of metal roofing options</p>
  </article>
  <article class="abs card" style="left:736px">
    <div class="card-photo" role="img" aria-label="Photo of a cream commercial building with burgundy roof and silos" style="background:linear-gradient(180deg,#dfe4ea,#7a3030 40%,#e6dccb 62%,#a9a9a4)"></div>
    <h4>Commercial<br>Applications</h4>
    <p>28 gauge panels are the thickest and strongest in the industry.</p>
  </article>
  <div class="btn btn-red" style="top:965px;left:547px;width:106px;height:30px">All Services</div>
</section>

<section class="abs stats">
  <div class="stat" style="left:326px"><b>10+</b><span>Years Experience</span></div>
  <div class="stat" style="left:518px"><b>600+</b><span>Completed Projects</span></div>
  <div class="stat" style="left:703px"><b>15+</b><span>Awards Received</span></div>
  <div class="stat" style="left:893px"><b>2000+</b><span>Satisfied Clients</span></div>
</section>

<section>
  <div class="abs projects-head" role="img" aria-label="Dark background photo of a building wall with windows"></div>
  <h2 class="heading" style="top:1268px;font-size:17px;color:var(--white)">Completed Projects</h2>
  <div class="abs grid">
    <div role="img" aria-label="Tan storage shed with brown roof" style="background:linear-gradient(180deg,#cfd6dc,#4a3b33 35%,#c9b48c 60%,#4f7a34)"></div>
    <div role="img" aria-label="Small shed at dusk" style="background:linear-gradient(180deg,#2d2d2e,#1c1d1c)"></div>
    <div role="img" aria-label="Cream two storey house with grey roof" style="background:linear-gradient(180deg,#cfdbe6,#7d8a93 35%,#e3e0cf 62%,#4f8a35)"></div>
    <div role="img" aria-label="Red and tan post frame building with porch" style="background:linear-gradient(180deg,#c8d2dc,#8c2c26 30%,#cdbfa6 60%,#6d6a62)"></div>
    <div role="img" aria-label="Red steel garage with white overhead door" style="background:linear-gradient(180deg,#d8dee3,#a82a24 35%,#b32c26 75%,#8a7a5c)"></div>
    <div role="img" aria-label="Tan shed among birch trees" style="background:linear-gradient(180deg,#9fbf7b,#b5a58a 45%,#8d7f66 75%,#5d7a3c)"></div>
    <div role="img" aria-label="Aerial view of a teal metal roof" style="background:linear-gradient(180deg,#5f7a4a,#2f9c94 40%,#37a79e 65%,#7a4a35)"></div>
    <div role="img" aria-label="Tan post frame house on green lawn" style="background:linear-gradient(180deg,#c4c6c2,#b8ad98 40%,#8b8170 58%,#4f7a34)"></div>
  </div>
  <div class="abs projects-foot" role="img" aria-label="Dark gravel ground background"></div>
  <div class="btn btn-red" style="top:1775px;left:547px;width:106px;height:30px">All Projects</div>
</section>

<section class="abs clients">
  <h2 class="heading" style="top:44px;font-size:17px">Our Client</h2>
  <p class="abs center" style="top:70px;left:400px;width:400px;font-size:8px;line-height:1.4;color:#ddd">Lorem ipsum dolor sit amet, consectetur adipiscing elit. Maecenas porta vulputate nulla vel efficitur. Orci varius natoque penatibus et magnis ridiculus mus.</p>
  <div class="heading-rule" style="top:102px"></div>
  <div class="avatar" style="top:138px;left:512px;width:42px;height:42px" role="img" aria-label="Client portrait"></div>
  <div class="avatar" style="top:131px;left:573px;width:54px;height:54px;border:2px solid #fff" role="img" aria-label="Client portrait"></div>
  <svg class="abs" style="top:186px;left:590px" width="20" height="12"><path d="M0 0h20L10 12z" fill="#fff"/></svg>
  <div class="avatar" style="top:138px;left:643px;width:42px;height:42px" role="img" aria-label="Client portrait"></div>
  <p class="abs center" style="top:210px;left:360px;width:480px;font-size:9.5px;line-height:1.5;color:#eee">Lorem ipsum dolor sit amet, consectetur adipiscing elit. Suspendisse commodo semper tristique. Suspendisse convallis ante urna, quis pharetra mauris suscipit ut. Pellentesque habitant morbi tristique senectus et malesuada fames ac turpis egestas sit amet posuere.</p>
  <p class="abs center" style="top:266px;width:1200px;font-family:'Raleway',sans-serif;font-weight:700;font-size:10px;text-transform:uppercase">Dana Whitfield</p>
  <span class="dot" style="left:582px;background:var(--red)"></span>
  <span class="dot" style="left:594px"></span>
  <span class="dot" style="left:606px"></span>
</section>

<section class="abs contact-band">
  <div class="contact-item" style="left:278px">
    <svg width="38" height="38" viewBox="0 0 40 40"><circle cx="20" cy="20" r="18" fill="none" stroke="#fff" stroke-width="2"/><path fill="#fff" d="M15 11c1 0 2 3 2.5 4.3.3.8-1.5 2-1.3 2.8.8 2.4 3 4.6 5.5 5.6.8.3 2-1.6 2.8-1.2C25.7 23 29 24.5 28.7 25.5 28 28 26 29.5 23.8 29 17 27.5 12 22 11 16c-.4-2.3 1.8-5 4-5z"/></svg>
    <div><small>Phone Number</small><strong>715-555-0142</strong></div>
  </div>
  <div class="contact-item" style="left:542px">
    <svg width="38" height="34" viewBox="0 0 38 34"><rect x="10" y="1" width="18" height="10" fill="#fff"/><rect x="1" y="12" width="36" height="14" rx="3" fill="#fff"/><rect x="9" y="20" width="20" height="13" fill="#fff" stroke="var(--red)" stroke-width="2"/></svg>
    <div><small>Fax</small><strong>715-555-0188</strong></div>
  </div>
  <div class="abs follow"><span>Follow Us:</span><i></i><i></i><i></i></div>
</section>

<footer>
  <div class="abs footer">
    <div class="abs" style="left:252px;top:70px;display:flex;align-items:center;gap:6px">
      <span style="width:10px;height:10px;background:var(--red)"></span>
      <span style="font-family:'Raleway',sans-serif;font-weight:800;font-size:16px;color:var(--red);text-transform:uppercase;line-height:1.05">Brantle<br>Panel</span>
    </div>
    <h5 style="left:432px">Useful Links</h5>
    <ul style="left:434px"><li>Home</li><li>About Us</li><li>Services</li><li>Gallery</li><li>Contact Us</li></ul>
    <h5 style="left:620px">Contact Us</h5>
    <ul style="left:620px;width:120px;text-align:center"><li>Call Us: 715-555-0142</li><li>Fax: 715-555-0188</li><li>info@example.com</li></ul>
    <h5 style="left:807px">Working Hours</h5>
    <div class="hours">
      <p>Our support available to help you 24 hours a day, seven days a week.</p>
      <div><span>Monday-Friday:</span><b>9am to 5pm</b></div>
      <div><span>Saturday:</span><b>10am to 2pm</b></div>
      <div><span>Sunday:</span><b>Closed</b></div>
    </div>
  </div>
  <div class="abs bottombar">
    <span>Copyright © 2019 www.brantlepanelinc.com</span>
    <nav><span>Our Services</span><span>Projects</span><span>Contact Us</span><span>Privacy Policy</span></nav>
  </div>
</footer>

</body>
</html>
```